Marlowick APP redesign and color change

I am looking for a new design for my app. Please see the attached current design.

Currently, I have a functioning app but the colors and design are awful!
The logo is great but the rest of the app needs a refresh.
(Logo hi res not yet available but will upload soon.)
New colors or anything that is cutting edge.

Basically: It is a secure social media app within a school system where the teachers, students and parents can text, exchange photos, plan curriculum, etc.

I NEED ONLY landing page with a new look!
Looking for one distinct design for the landing page with new look.
The developer will apply this one design towards the rest of the pages/app screens.

Because part of the social media I need the feel and look of what is now the trend. Something that will attract and keep the client(s) interested. I am really leaving all the creative work to the designer and open to any suggestions.
Updates

Target Market(s)

Schools, community, teachers, students, colleges, sport teams

Industry/Entity Type

Non Profit

Font styles to use
Serif
Sans Serif

Colors

Designer to choose colors to be used in the design.

Requirements
Must have
• Sharp, trendy, millennial feel
Nice to have
• Up to designer
Should not have
• Up to designer

```html
<!DOCTYPE html>
<html lang="en">
<head>
<meta charset="utf-8">
<title>Marlowick – Conversations</title>
<link rel="stylesheet" href="https://fonts.googleapis.com/css2?family=Inter:wght@400;500;600&display=swap">
<style>
  :root {
    --yellow: #ffc81a;
    --search: #d3a81b;
    --ink: #1f1f1f;
    --muted: #8a8a8a;
    --row: #ffffff;
    --avatar-well: #efefef;
    --divider: #dcdcdc;
    --tab-bar: #242021;
    --tab-active: #000000;
    --white: #ffffff;
  }
  * { box-sizing: border-box; margin: 0; padding: 0; }
  html, body { width: 675px; height: 1200px; overflow: hidden; }
  body {
    position: relative;
    background: var(--yellow);
    font-family: "Inter", "Helvetica Neue", Arial, sans-serif;
    color: var(--ink);
  }
  .status-bar {
    position: absolute; top: 0; left: 0; right: 0; height: 36px;
    display: flex; align-items: center; justify-content: space-between;
    padding: 0 12px; font-size: 17px; font-weight: 500;
  }
  .status-left, .status-right { display: flex; align-items: center; gap: 5px; }
  .status-time { position: absolute; left: 0; right: 0; text-align: center; }
  .nav-bar {
    position: absolute; top: 52px; left: 0; right: 0; height: 54px;
    display: flex; align-items: center; justify-content: center;
  }
  .nav-title { font-size: 32px; font-weight: 500; letter-spacing: -0.2px; }
  .nav-back { position: absolute; left: 38px; top: 13px; }
  .nav-next { position: absolute; right: 40px; font-size: 20px; font-weight: 600; }
  .conversations {
    position: absolute; top: 148px; left: 41px; width: 594px;
  }
  .search {
    height: 81px; background: var(--search);
    display: flex; align-items: center; justify-content: space-between;
    padding: 0 30px 0 27px;
  }
  .search-placeholder { color: var(--white); font-size: 17px; }
  .thread {
    height: 146.7px; display: flex; background: var(--row);
    border-bottom: 1px solid var(--divider);
  }
  .thread-avatar-well {
    width: 147px; background: var(--avatar-well);
    display: flex; align-items: center; justify-content: center;
  }
  .thread-avatar { width: 112px; height: 112px; border-radius: 9px; }
  .thread-text { flex: 1; padding-left: 43px; display: flex; flex-direction: column; justify-content: center; }
  .thread-name { font-size: 31px; font-weight: 500; line-height: 1.15; }
  .thread-preview { font-size: 25px; color: var(--muted); line-height: 1.2; }
  .thread-chevron { width: 60px; display: flex; align-items: center; }
  .bottom-fade {
    position: absolute; left: 0; right: 0; top: 1040px; height: 69px;
    background: linear-gradient(to bottom, rgba(40,30,0,0), rgba(40,30,0,0.18));
  }
  .tab-bar {
    position: absolute; left: 0; right: 0; bottom: 0; height: 91px;
    background: var(--tab-bar); display: flex;
  }
  .tab { flex: 1; display: flex; align-items: center; justify-content: center; }
  .tab.is-active { background: var(--tab-active); flex: 0 0 164px; }
</style>
</head>
<body>
  <div class="status-bar">
    <div class="status-left">
      <svg width="66" height="12" viewBox="0 0 66 12" fill="#000"><circle cx="6" cy="6" r="5"/><circle cx="19" cy="6" r="5"/><circle cx="32" cy="6" r="5"/><circle cx="45" cy="6" r="5"/><circle cx="58" cy="6" r="5"/></svg>
      <svg width="20" height="15" viewBox="0 0 20 15" fill="none" stroke="#000" stroke-width="2.2" stroke-linecap="round"><path d="M2 5.5a11 11 0 0 1 16 0"/><path d="M5 8.8a7 7 0 0 1 10 0"/><circle cx="10" cy="12.5" r="1.3" fill="#000"/></svg>
    </div>
    <div class="status-time">9:41 AM</div>
    <div class="status-right">
      <span>100%</span>
      <svg width="44" height="18" viewBox="0 0 44 18"><rect x="1" y="1" width="38" height="16" rx="3" fill="none" stroke="#000" stroke-width="1.5"/><rect x="3" y="3" width="34" height="12" rx="1.5" fill="#000"/><rect x="40.5" y="6" width="2.5" height="6" rx="1" fill="#000"/></svg>
    </div>
  </div>

  <header class="nav-bar">
    <svg class="nav-back" width="20" height="30" viewBox="0 0 20 30" fill="none" stroke="#1f1f1f" stroke-width="4" stroke-linecap="round" stroke-linejoin="round"><path d="M16 3 4 15l12 12"/></svg>
    <h1 class="nav-title">Conversations</h1>
    <span class="nav-next">Next</span>
  </header>

  <main class="conversations">
    <div class="search">
      <span class="search-placeholder">name search...</span>
      <svg width="32" height="32" viewBox="0 0 32 32" fill="none" stroke="#fff" stroke-width="3.2" stroke-linecap="round"><circle cx="13" cy="13" r="10"/><path d="M20.5 20.5 29 29"/></svg>
    </div>

    <div class="thread">
      <div class="thread-avatar-well"><div class="thread-avatar" role="img" aria-label="Profile photo of a young man" style="background:linear-gradient(160deg,#c9d1d6,#7b6e63 60%,#2e2a28)"></div></div>
      <div class="thread-text"><span class="thread-name">danny dee</span><span class="thread-preview">hello is this working</span></div>
      <div class="thread-chevron"><svg width="20" height="30" viewBox="0 0 20 30" fill="none" stroke="#ffc81a" stroke-width="4" stroke-linecap="round" stroke-linejoin="round"><path d="M4 3l12 12L4 27"/></svg></div>
    </div>
    <div class="thread">
      <div class="thread-avatar-well"><div class="thread-avatar" role="img" aria-label="Profile photo of a smiling young woman" style="background:linear-gradient(160deg,#a89a86,#8a5a3e 55%,#d9b9a3)"></div></div>
      <div class="thread-text"><span class="thread-name">basketball</span><span class="thread-preview">Blah</span></div>
      <div class="thread-chevron"><svg width="20" height="30" viewBox="0 0 20 30" fill="none" stroke="#ffc81a" stroke-width="4" stroke-linecap="round" stroke-linejoin="round"><path d="M4 3l12 12L4 27"/></svg></div>
    </div>
    <div class="thread">
      <div class="thread-avatar-well"><div class="thread-avatar" role="img" aria-label="Profile photo of a girl with long hair" style="background:linear-gradient(160deg,#8c5a3a,#b07a55 50%,#e4c2a6)"></div></div>
      <div class="thread-text"><span class="thread-name">danny dee 2.0</span><span class="thread-preview">hi</span></div>
      <div class="thread-chevron"><svg width="20" height="30" viewBox="0 0 20 30" fill="none" stroke="#ffc81a" stroke-width="4" stroke-linecap="round" stroke-linejoin="round"><path d="M4 3l12 12L4 27"/></svg></div>
    </div>
    <div class="thread">
      <div class="thread-avatar-well"><div class="thread-avatar" role="img" aria-label="Profile photo of a smiling young man outdoors" style="background:linear-gradient(160deg,#5e8a3a,#b88d70 50%,#4f7aa8)"></div></div>
      <div class="thread-text"><span class="thread-name">Talor, Ned</span><span class="thread-preview">Room 2434 about 7am.</span></div>
      <div class="thread-chevron"><svg width="20" height="30" viewBox="0 0 20 30" fill="none" stroke="#ffc81a" stroke-width="4" stroke-linecap="round" stroke-linejoin="round"><path d="M4 3l12 12L4 27"/></svg></div>
    </div>
    <div class="thread">
      <div class="thread-avatar-well"><div class="thread-avatar" role="img" aria-label="Profile photo of a woman in sunglasses" style="background:linear-gradient(160deg,#3a3330,#a9786a 55%,#5a4e4a)"></div></div>
      <div class="thread-text"><span class="thread-name">Ned, Faith</span><span class="thread-preview">Faith,</span></div>
      <div class="thread-chevron"><svg width="20" height="30" viewBox="0 0 20 30" fill="none" stroke="#ffc81a" stroke-width="4" stroke-linecap="round" stroke-linejoin="round"><path d="M4 3l12 12L4 27"/></svg></div>
    </div>
    <div class="thread">
      <div class="thread-avatar-well"><div class="thread-avatar" role="img" aria-label="Profile photo of a smiling blonde woman" style="background:linear-gradient(160deg,#b89a6a,#d8b48a 50%,#6e5a48)"></div></div>
      <div class="thread-text"><span class="thread-name">Ned, Gareth</span><span class="thread-preview">You are welcome</span></div>
      <div class="thread-chevron"><svg width="20" height="30" viewBox="0 0 20 30" fill="none" stroke="#ffc81a" stroke-width="4" stroke-linecap="round" stroke-linejoin="round"><path d="M4 3l12 12L4 27"/></svg></div>
    </div>
  </main>

  <div class="bottom-fade"></div>

  <nav class="tab-bar">
    <div class="tab is-active" aria-label="Conversations">
      <svg width="52" height="44" viewBox="0 0 52 44" fill="none" stroke="#fff" stroke-width="2.4" stroke-linejoin="round"><path d="M20 4h28v20h-6v7l-7-7H20z"/><path d="M20 14H4v20h6v7l7-7h14v-6"/><circle cx="28" cy="14" r="1" fill="#fff"/><circle cx="34" cy="14" r="1" fill="#fff"/><circle cx="40" cy="14" r="1" fill="#fff"/></svg>
    </div>
    <div class="tab" aria-label="Dashboard">
      <svg width="44" height="44" viewBox="0 0 44 44" fill="none" stroke="#fff" stroke-width="2.4"><rect x="2" y="2" width="18" height="18" rx="4"/><rect x="24" y="2" width="18" height="18" rx="4"/><rect x="2" y="24" width="18" height="18" rx="4"/><rect x="24" y="24" width="18" height="18" rx="4"/></svg>
    </div>
    <div class="tab" aria-label="Directory">
      <svg width="34" height="44" viewBox="0 0 34 44" fill="none" stroke="#fff" stroke-width="2.4" stroke-linejoin="round"><rect x="2" y="2" width="30" height="40" rx="2"/><path d="M9 2v40"/><path d="M32 16l-6 6 6 6"/></svg>
    </div>
    <div class="tab" aria-label="Settings">
      <svg width="46" height="46" viewBox="0 0 46 46" fill="none" stroke="#fff" stroke-width="2.4" stroke-linejoin="round"><path d="M19.5 3h7l1.2 5.4 3.6 1.5 4.7-3 4.9 4.9-3 4.7 1.5 3.6 5.4 1.2v7l-5.4 1.2-1.5 3.6 3 4.7-4.9 4.9-4.7-3-3.6 1.5-1.2 5.4h-7l-1.2-5.4-3.6-1.5-4.7 3-4.9-4.9 3-4.7-1.5-3.6L3 26.5v-7l5.4-1.2 1.5-3.6-3-4.7 4.9-4.9 4.7 3 3.6-1.5z"/><circle cx="23" cy="23" r="7"/></svg>
    </div>
  </nav>
</body>
</html>
```